Flyer design

We need a new flyer designed. We are not happy with our current design. We want to keep the pictures and basic info, just new design.

Target Market(s)

primarily multi family and HOA,s

Industry/Entity Type

Construction Company

Requirements
Must have
• Must have photos uploaded and use the text on the previous flyer. (also uploaded)

```html
<!DOCTYPE html>
<html lang="en">
<head>
<meta charset="utf-8">
<title>Stonewell Construction Services Inc. – Flyer</title>
<link rel="stylesheet" href="https://fonts.googleapis.com/css2?family=Archivo:wght@800&family=Roboto:wght@400;500&family=Roboto+Condensed:wght@300;700&display=swap">
<style>
  :root {
    --blue: #1a56e0;
    --blue-deep: #0a34a8;
    --blue-band: #0b2f97;
    --grey-dark: #2f3033;
    --grey-mid: #55575b;
    --white: #ffffff;
    --ink-soft: #6b6f76;
    --photo-warm: #d9c7ae;
    --photo-light: #f1ebe2;
  }
  * { margin: 0; padding: 0; box-sizing: border-box; }
  html, body { width: 707px; height: 1200px; overflow: hidden; background: #e9e9e9; }
  .flyer { position: relative; width: 707px; height: 1200px; overflow: hidden; font-family: "Roboto", Arial, sans-serif; color: var(--white); }
  .flyer-shapes { position: absolute; inset: 0; }
  .brand { position: absolute; top: 44px; left: 0; right: 0; display: flex; justify-content: center; align-items: center; gap: 12px; }
  .brand-mark { width: 26px; height: 26px; background: var(--blue); }
  .brand-name { font-family: "Roboto Condensed", Arial, sans-serif; font-weight: 700; font-size: 30px; color: var(--blue); letter-spacing: .3px; }
  .advantage { position: absolute; left: 36px; top: 486px; }
  .advantage-title { font-family: "Archivo", Arial, sans-serif; font-weight: 800; font-size: 42px; line-height: 46px; text-transform: uppercase; letter-spacing: .5px; }
  .advantage-list { list-style: none; margin-top: 24px; }
  .advantage-list li, .services-list li { display: flex; align-items: center; gap: 12px; font-size: 14.5px; height: 29px; }
  .cone { width: 11px; height: 13px; flex: none; }
  .services { position: absolute; right: 30px; top: 708px; text-align: right; }
  .services-title { font-family: "Roboto Condensed", Arial, sans-serif; text-transform: uppercase; font-size: 44px; line-height: 44px; }
  .services-title .light { font-weight: 300; display: block; }
  .services-title .bold { font-weight: 700; display: block; }
  .services-list { list-style: none; margin-top: 22px; }
  .services-list li { justify-content: flex-end; }
  .offices { position: absolute; left: 28px; top: 1024px; display: flex; gap: 30px; }
  .office-name { font-family: "Roboto Condensed", Arial, sans-serif; font-weight: 700; font-size: 16px; display: flex; align-items: center; gap: 6px; }
  .office-lines { padding-left: 24px; font-size: 13px; line-height: 17px; margin-top: 4px; }
  .contact { position: absolute; left: 28px; top: 1120px; display: flex; align-items: center; gap: 8px; }
  .contact-phone { font-family: "Roboto Condensed", Arial, sans-serif; font-weight: 700; font-size: 24px; }
  .contact-sep { font-size: 24px; }
  .contact-web { font-size: 15px; }
  .tagline { position: absolute; left: 0; right: 0; bottom: 0; height: 36px; display: flex; justify-content: center; align-items: center; font-family: "Roboto Condensed", Arial, sans-serif; font-weight: 700; font-size: 17px; letter-spacing: .3px; }
  .icon { width: 18px; height: 18px; flex: none; }
</style>
</head>
<body>
<main class="flyer">
  <svg class="flyer-shapes" width="707" height="1200" viewBox="0 0 707 1200" aria-hidden="false">
    <defs>
      <linearGradient id="interior" x1="0" y1="0" x2="1" y2="1">
        <stop offset="0" stop-color="#f3efe8"/>
        <stop offset=".45" stop-color="#e2d3bd"/>
        <stop offset=".75" stop-color="#b79a7a"/>
        <stop offset="1" stop-color="#8e7358"/>
      </linearGradient>
      <linearGradient id="header-fade" x1="0" y1="0" x2="0" y2="1">
        <stop offset="0" stop-color="#fff" stop-opacity="1"/>
        <stop offset=".55" stop-color="#fff" stop-opacity=".85"/>
        <stop offset="1" stop-color="#fff" stop-opacity="0"/>
      </linearGradient>
      <linearGradient id="blue-field" x1="0" y1="0" x2="1" y2="1">
        <stop offset="0" stop-color="#1f5cf0"/>
        <stop offset="1" stop-color="#0c3fc0"/>
      </linearGradient>
      <linearGradient id="grey-panel" x1="0" y1="0" x2="0" y2="1">
        <stop offset="0" stop-color="#4a4c50"/>
        <stop offset="1" stop-color="#242528"/>
      </linearGradient>
    </defs>

    <rect class="hero-photo" x="0" y="0" width="707" height="560" fill="url(#interior)" role="img" aria-label="Photo of a bright remodeled living room with large windows, ceiling fans and lounge furniture"/>
    <rect x="0" y="0" width="707" height="200" fill="url(#header-fade)"/>

    <path class="blue-field" d="M707,420 L0,830 L0,1200 L707,1200 Z" fill="url(#blue-field)"/>
    <path d="M707,420 L0,830" stroke="#fff" stroke-width="3"/>

    <path class="advantage-panel" d="M0,400 L330,290 Q350,284 368,296 L600,470 Q612,482 602,496 L190,922 Q160,955 128,930 L0,830 Z" fill="url(#grey-panel)"/>

    <g class="project-photos" stroke="#fff" stroke-width="5">
      <polygon points="104,262 151,290 151,346 104,374 57,346 57,290" fill="#8a9aa8" role="img" aria-label="Photo of a roofer installing shingles"/>
      <polygon points="266,374 313,402 313,458 266,486 219,458 219,402" fill="#6e6f73" role="img" aria-label="Photo of a worker spreading asphalt"/>
      <polygon points="444,511 491,539 491,595 444,623 397,595 397,539" fill="#a49886" role="img" aria-label="Photo of an interior renovation in progress"/>
    </g>

    <rect class="tagline-band" x="0" y="1164" width="707" height="36" fill="var(--blue-band)"/>
    <rect x="0" y="1162" width="707" height="2" fill="#5f86ff"/>
  </svg>

  <header class="brand">
    <span class="brand-mark"></span>
    <span class="brand-name">Stonewell Construction Services Inc.</span>
  </header>

  <section class="advantage">
    <h1 class="advantage-title">The<br>Stonewell<br>Advantage</h1>
    <ul class="advantage-list">
      <li><svg class="cone" viewBox="0 0 11 13"><path d="M5.5 0 L9 11 H2 Z M0 11 H11 V13 H0 Z" fill="#fff"/></svg>Hands on approach</li>
      <li><svg class="cone" viewBox="0 0 11 13"><path d="M5.5 0 L9 11 H2 Z M0 11 H11 V13 H0 Z" fill="#fff"/></svg>High Level of communication with client</li>
      <li><svg class="cone" viewBox="0 0 11 13"><path d="M5.5 0 L9 11 H2 Z M0 11 H11 V13 H0 Z" fill="#fff"/></svg>Daily or weekly updates on every project</li>
      <li><svg class="cone" viewBox="0 0 11 13"><path d="M5.5 0 L9 11 H2 Z M0 11 H11 V13 H0 Z" fill="#fff"/></svg>Competitive pricing</li>
      <li><svg class="cone" viewBox="0 0 11 13"><path d="M5.5 0 L9 11 H2 Z M0 11 H11 V13 H0 Z" fill="#fff"/></svg>Due diligence</li>
      <li><svg class="cone" viewBox="0 0 11 13"><path d="M5.5 0 L9 11 H2 Z M0 11 H11 V13 H0 Z" fill="#fff"/></svg>Single source for all needs</li>
    </ul>
  </section>

  <section class="services">
    <h2 class="services-title"><span class="light">Services</span><span class="bold">We Provide</span></h2>
    <ul class="services-list">
      <li>Roof replacements<svg class="cone" viewBox="0 0 11 13"><path d="M5.5 0 L9 11 H2 Z M0 11 H11 V13 H0 Z" fill="#fff"/></svg></li>
      <li>Consulting services<svg class="cone" viewBox="0 0 11 13"><path d="M5.5 0 L9 11 H2 Z M0 11 H11 V13 H0 Z" fill="#fff"/></svg></li>
      <li>Budget proposals<svg class="cone" viewBox="0 0 11 13"><path d="M5.5 0 L9 11 H2 Z M0 11 H11 V13 H0 Z" fill="#fff"/></svg></li>
      <li>Exterior siding and carpentry<svg class="cone" viewBox="0 0 11 13"><path d="M5.5 0 L9 11 H2 Z M0 11 H11 V13 H0 Z" fill="#fff"/></svg></li>
      <li>Exterior/interior paint<svg class="cone" viewBox="0 0 11 13"><path d="M5.5 0 L9 11 H2 Z M0 11 H11 V13 H0 Z" fill="#fff"/></svg></li>
      <li>Office and clubhouse remodeling<svg class="cone" viewBox="0 0 11 13"><path d="M5.5 0 L9 11 H2 Z M0 11 H11 V13 H0 Z" fill="#fff"/></svg></li>
      <li>Fire and flood damage build back<svg class="cone" viewBox="0 0 11 13"><path d="M5.5 0 L9 11 H2 Z M0 11 H11 V13 H0 Z" fill="#fff"/></svg></li>
      <li>Large scale interior renovations<svg class="cone" viewBox="0 0 11 13"><path d="M5.5 0 L9 11 H2 Z M0 11 H11 V13 H0 Z" fill="#fff"/></svg></li>
      <li>Dog parks<svg class="cone" viewBox="0 0 11 13"><path d="M5.5 0 L9 11 H2 Z M0 11 H11 V13 H0 Z" fill="#fff"/></svg></li>
      <li>Asphalt paving<svg class="cone" viewBox="0 0 11 13"><path d="M5.5 0 L9 11 H2 Z M0 11 H11 V13 H0 Z" fill="#fff"/></svg></li>
    </ul>
  </section>

  <section class="offices">
    <div class="office">
      <p class="office-name"><svg class="icon" viewBox="0 0 18 18"><circle cx="9" cy="9" r="8" fill="none" stroke="#fff" stroke-width="1.5"/><path d="M9 4a3 3 0 0 0-3 3c0 2.3 3 6 3 6s3-3.7 3-6a3 3 0 0 0-3-3z" fill="#fff"/></svg>California Address</p>
      <p class="office-lines">418 Harbor View Dr.<br>Suite 210 Laguna Vista,<br>CA. 90210</p>
    </div>
    <div class="office">
      <p class="office-name"><svg class="icon" viewBox="0 0 18 18"><circle cx="9" cy="9" r="8" fill="none" stroke="#fff" stroke-width="1.5"/><path d="M9 4a3 3 0 0 0-3 3c0 2.3 3 6 3 6s3-3.7 3-6a3 3 0 0 0-3-3z" fill="#fff"/></svg>Texas Address</p>
      <p class="office-lines">1870 Cedar Creek Rd.<br>Suite 205-310<br>Oakfield TX. 75001</p>
    </div>
  </section>

  <div class="contact">
    <svg class="icon" viewBox="0 0 18 18"><path d="M4 2l3 3-1.5 2a9 9 0 0 0 5.5 5.5L13 11l3 3-2 2.5C8 16 2 10 1.5 4z" fill="#fff"/></svg>
    <span class="contact-phone">(555) 014-2290</span>
    <span class="contact-sep">|</span>
    <svg class="icon" viewBox="0 0 18 18"><circle cx="9" cy="9" r="7.5" fill="none" stroke="#fff" stroke-width="1.5"/><circle cx="9" cy="9" r="3.5" fill="#fff"/></svg>
    <span class="contact-web">www.stonewellconstruction.com</span>
  </div>

  <footer class="tagline">General Contractor | Multifamily | Commercial | Residential | Due Diligence</footer>
</main>
</body>
</html>
```